Business card design needed

Card needs to say

Maren Fuldwick
Investor - Solutions - Development

My business is in property deals. I would like the words above to be on the card. I have attached a logo for you to copy/recreate.
On the back you could list the following:

Hearthway Property Solutions

Thankyou, Maren

Target Market(s)

people wanting to get into the property market, desperate sellers, Mums & Dads wanting to help their kids to purchase a property. People who want to create wealth. People who are stuck and need a solution.

Industry/Entity Type

Business

Contact Information for Business Card

T: 0431 205 774
F: (07) 3842 1597
E: maren47@vexlo.com.au

Requirements
Must have
• Simple and effective.
Look like I am here to help
Should not have
• Should not look like a realestate agent

```html
<!DOCTYPE html>
<html lang="en">
<head>
<meta charset="utf-8">
<title>Maren Fuldwick – Business Card</title>
<link rel="stylesheet" href="https://fonts.googleapis.com/css2?family=Archivo+Black&family=Arimo:wght@400;700&display=swap">
<style>
  :root {
    --bg: #2a2a2a;
    --card: #ffffff;
    --card-shade: #f1f1f1;
    --blue: #1b8fcf;
    --green: #7cc242;
    --ink: #333333;
    --rule: #8a8a8a;
  }
  * { margin: 0; padding: 0; box-sizing: border-box; }
  html, body {
    width: 1200px;
    height: 900px;
    overflow: hidden;
    background: var(--bg);
  }
  .stage {
    width: 1200px;
    height: 900px;
    display: flex;
    flex-direction: column;
    align-items: center;
    justify-content: center;
    gap: 40px;
  }
  .card {
    width: 700px;
    height: 390px;
    background: linear-gradient(160deg, var(--card) 0%, var(--card-shade) 100%);
    position: relative;
    font-family: "Arimo", Arial, sans-serif;
  }

  /* Back side */
  .contact {
    position: absolute;
    left: 110px;
    top: 200px;
    width: 230px;
    text-align: right;
    color: var(--blue);
    font-size: 15px;
    line-height: 22px;
    letter-spacing: 0.5px;
  }
  .back-mark {
    position: absolute;
    left: 352px;
    top: 196px;
    width: 44px;
    height: 44px;
    border: 3px solid var(--blue);
    border-radius: 50%;
  }
  .back-tagline {
    position: absolute;
    left: 408px;
    top: 198px;
    color: var(--blue);
    font-size: 14px;
    letter-spacing: 0.4px;
    white-space: nowrap;
  }
  .sign-off {
    position: absolute;
    right: 70px;
    top: 110px;
    text-align: right;
    color: var(--blue);
    font-size: 14px;
    line-height: 20px;
  }

  /* Front side */
  .brand {
    position: absolute;
    left: 0;
    right: 0;
    top: 80px;
    display: flex;
    align-items: center;
    justify-content: center;
    gap: 14px;
  }
  .brand-dot {
    width: 30px;
    height: 30px;
    border-radius: 50%;
    background: var(--green);
  }
  .brand-name {
    font-family: "Arimo", Arial, sans-serif;
    font-weight: 700;
    font-size: 38px;
    color: var(--blue);
  }
  .identity {
    position: absolute;
    left: 0;
    right: 0;
    top: 200px;
    text-align: center;
  }
  .person-name {
    font-family: "Archivo Black", "Arial Black", sans-serif;
    font-size: 50px;
    font-weight: 400;
    color: var(--blue);
    letter-spacing: -0.5px;
    line-height: 1;
  }
  .services {
    display: inline-block;
    margin-top: 6px;
    padding: 0 6px 6px;
    border-bottom: 1.5px solid var(--rule);
    font-size: 27px;
    color: var(--ink);
    letter-spacing: 0.3px;
  }
</style>
</head>
<body>
<main class="stage">
  <section class="card card-back" aria-label="Card back">
    <div class="contact">
      <p>T : 0431 205 774</p>
      <p>F : (07) 3842 1597</p>
      <p>E : maren47@vexlo.com.au</p>
    </div>
    <div class="back-mark" aria-hidden="true"></div>
    <p class="back-tagline">Hearthway Property Solutions</p>
    <p class="sign-off">Thank You,<br>Maren</p>
  </section>

  <section class="card card-front" aria-label="Card front">
    <div class="brand">
      <span class="brand-dot" aria-hidden="true"></span>
      <span class="brand-name">Hearthway</span>
    </div>
    <div class="identity">
      <h1 class="person-name">Maren Fuldwick</h1>
      <p class="services">Investor . Solutions . Development</p>
    </div>
  </section>
</main>
</body>
</html>
```